Resident Guide for Senior Living Community

I need to create an informational magazine for residents that live in an Assisted Living community. This magazine is designed to educate the resident about the different service options and features that the community provides. I don't want to use any of the pictures in the Word Document - please use the uploaded picture instead. The final design should be both informational and elegant. The text in the word document is the actual text that needs to be used in the Resident Guide. Thanks!

Target Market(s)

Senior citizens and adult children (55 - 65 years old)

Industry/Entity Type

Assisted Living

Requirements
Must have
• Must be elegant - think Vellmore Orsay. Needs to have a lot of pictures and the logo must be used. The logo is the Plaque that says The Pellow Court.
Nice to have
• The Word doucment is the old Resident Guide - we are looking for a refresh using the same content.
Should not have
• please do not use any pictures from the Word Document other than the Logo.

```html
<!DOCTYPE html>
<html lang="en">
<head>
<meta charset="utf-8">
<title>The Pellow Court — Resident Information</title>
<link href="https://fonts.googleapis.com/css2?family=Lato:wght@300;400&display=swap" rel="stylesheet">
<style>
  :root {
    --backdrop: #ececec;
    --paper: #ffffff;
    --gold: #a8882c;
    --gold-soft: #b39a52;
  }
  * { margin: 0; padding: 0; box-sizing: border-box; }
  html, body {
    width: 1200px;
    height: 1000px;
    overflow: hidden;
    background: var(--backdrop);
  }
  .spread {
    position: relative;
    width: 1200px;
    height: 1000px;
    font-family: 'Lato', sans-serif;
  }
  .page {
    position: absolute;
    top: 177px;
    width: 409px;
    height: 576px;
    background: var(--paper);
    box-shadow: 0 1px 3px rgba(0,0,0,0.12);
  }
  .page--front { left: 173px; }
  .page--back  { left: 633px; }

  .brand-name {
    position: absolute;
    left: 0;
    right: 0;
    text-align: center;
    color: var(--gold);
    font-weight: 400;
    text-transform: uppercase;
    letter-spacing: 0.06em;
  }
  .page--front .brand-name {
    top: 232px;
    font-size: 22px;
  }
  .page--back .brand-name {
    top: 404px;
    font-size: 13px;
  }

  .front-title {
    position: absolute;
    left: 0;
    right: 0;
    top: 525px;
    text-align: center;
    color: var(--gold);
    font-size: 13px;
    font-weight: 400;
    letter-spacing: 0.03em;
  }

  .contact {
    position: absolute;
    left: 0;
    right: 0;
    top: 463px;
    text-align: center;
    color: var(--gold-soft);
    font-size: 9px;
    font-weight: 300;
    line-height: 12.5px;
    letter-spacing: 0.02em;
  }
  .contact__heading {
    text-transform: uppercase;
    margin-bottom: 12px;
  }
  .contact__group + .contact__group { margin-top: 12px; }
  .contact__divider { padding: 0 4px; }
</style>
</head>
<body>
  <main class="spread">
    <section class="page page--front">
      <p class="brand-name">The Pellow Court</p>
      <h1 class="front-title">RESIDENT INFORMATION</h1>
    </section>

    <section class="page page--back">
      <p class="brand-name">The Pellow Court</p>
      <div class="contact">
        <p class="contact__heading">Contact Information:</p>
        <div class="contact__group">
          <p>www.ThePellowCourt.com<span class="contact__divider">|</span>hello@ThePellowCourt.com</p>
          <p>404.555.0142</p>
        </div>
        <div class="contact__group">
          <p>www.PellowCourtNorth.com</p>
          <p>(770) 555-0187</p>
        </div>
      </div>
    </section>
  </main>
</body>
</html>
```